label design needed for beef product

i need a simple nice packaging design like these
https://www.brindlemart-shop.example/Ridge-Larder-Gelatin-Natural-Powder/dp/K7QX4LT915/ref=sr_1_3_a_it?ie=UTF8&qid=1500000001&sr=8-3&keywords=beef+gelatin+powder

My company name is TIRP
See logo
https://www.brindlemart-shop.example/Vitamin-Hyaluronic-Nutrient-Lighten-Circles/dp/K3PZ82HDWQ/ref=sr_1_3_a_it?ie=UTF8&qid=1500000002&sr=8-3&keywords=tirp&th=1

i must have the same logo on the label design ,
see attached for the front wording and the back

the facts or the same as the now

Target Market(s)

Brindlemart,

Industry/Entity Type

Health And Wellness

Font styles to use
Serif
Sans Serif

Colors

Designer to choose colors to be used in the design.

Requirements
Must have
• the logo like it is on the following link
• https://www.brindlemart-shop.example/Vitamin-Hyaluronic-Nutrient-Lighten-Circles/dp/K3PZ82HDWQ/ref=sr_1_3_a_it?ie=UTF8&qid=1500000002&sr=8-3&keywords=tirp&th=1
• I need a professional nice listing
Nice to have
• a nice background the packaging size will be the same as now see below
• https://www.brindlemart-shop.example/Ridge-Larder-Gelatin-Natural-Powder/dp/K7QX4LT915/ref=sr_1_3_a_it?ie=UTF8&qid=1500000003&sr=8-3&keywords=beef+gelatin
• i like that design but i want much more professional to it
Should not have
• will discuss

```html
<!DOCTYPE html>
<html lang="en">
<head>
<meta charset="utf-8">
<title>TIRP Unflavored Beef Gelatin Powder Label</title>
<link rel="stylesheet" href="https://fonts.googleapis.com/css2?family=Josefin+Sans:wght@300;400&family=Lato:wght@400;700&family=Lobster&display=swap">
<style>
  :root {
    --backdrop: #161616;
    --panel-light: #57575a;
    --panel-dark: #3a3a3c;
    --frame-pink: #b0789f;
    --brand-purple: #a8739c;
    --soft-pink: #dcc2d6;
    --text-white: #ffffff;
    --text-grey: #e6e6e6;
    --rule: #9a9a9c;
  }
  * { box-sizing: border-box; margin: 0; padding: 0; }
  html, body {
    width: 1200px; height: 999px; overflow: hidden;
    background: var(--backdrop);
  }
  .label {
    position: absolute; left: 250px; top: 40px;
    width: 700px; height: 920px;
    background: radial-gradient(ellipse at 50% 40%, var(--panel-light) 0%, var(--panel-dark) 80%);
    font-family: "Lato", sans-serif;
    color: var(--text-white);
    text-align: center;
  }
  .label-frame {
    position: absolute; inset: 14px;
    border: 1.5px solid var(--frame-pink);
  }
  .brand-tab {
    position: absolute; left: 145px; top: 0;
    width: 410px; height: 225px;
  }
  .brand-tab svg { position: absolute; inset: 0; }
  .brand-name {
    position: absolute; left: 0; right: 0; top: 70px;
    display: flex; align-items: center; justify-content: center; gap: 22px;
    font-family: "Lato", sans-serif; font-weight: 400;
    font-size: 62px; color: var(--brand-purple); letter-spacing: 2px;
  }
  .brand-dot {
    width: 40px; height: 40px; border-radius: 50%;
    border: 4px solid var(--brand-purple);
  }
  .ruled {
    position: absolute; left: 75px; right: 75px;
    display: flex; align-items: center; gap: 14px;
  }
  .ruled::before, .ruled::after {
    content: ""; flex: 1; height: 1.5px; background: var(--text-grey);
  }
  .variant {
    top: 282px;
    font-family: "Josefin Sans", sans-serif; font-weight: 400;
    font-size: 32px; letter-spacing: 3px; color: var(--text-white);
  }
  .variant .knob {
    width: 14px; height: 14px; border-radius: 50%;
    border: 1.5px solid var(--text-grey); flex: none;
  }
  .product-name {
    position: absolute; left: 0; right: 0; top: 340px;
    font-family: "Josefin Sans", sans-serif; font-weight: 300;
    font-size: 150px; line-height: 1; color: var(--soft-pink);
  }
  .product-form {
    top: 462px;
    font-family: "Josefin Sans", sans-serif; font-weight: 400;
    font-size: 40px; letter-spacing: 8px;
  }
  .benefits {
    position: absolute; left: 140px; right: 140px; top: 555px;
    padding: 6px 0;
    border-top: 1px solid var(--rule); border-bottom: 1px solid var(--rule);
    font-size: 24px; line-height: 31px; color: var(--text-grey);
  }
  .purity {
    position: absolute; left: 0; right: 0; top: 672px;
    font-weight: 700; font-size: 27px; line-height: 32px; color: var(--soft-pink);
  }
  .tagline {
    position: absolute; left: 0; right: 0; top: 790px;
    font-family: "Lobster", cursive; font-size: 42px; color: var(--text-white);
  }
  .net-weight {
    position: absolute; left: 0; right: 0; top: 866px;
    font-weight: 700; font-size: 23px;
  }
</style>
</head>
<body>
  <main class="label">
    <div class="label-frame"></div>

    <div class="brand-tab">
      <svg width="410" height="225" viewBox="0 0 410 225" aria-hidden="true">
        <path d="M0 0 H410 V225 Q300 185 205 190 Q110 185 0 225 Z" fill="#ffffff"/>
      </svg>
      <div class="brand-name"><span class="brand-dot"></span>TIRP</div>
    </div>

    <div class="ruled variant"><span class="knob"></span>UNFLAVORED&nbsp; BEEF<span class="knob"></span></div>
    <h1 class="product-name">GELATIN</h1>
    <div class="ruled product-form">powder</div>

    <ul class="benefits" style="list-style:none">
      <li>Stimulates Collagen production</li>
      <li>Reduces fine lines and wrinkles</li>
      <li>Strengthens hair, nails &amp; teeth</li>
    </ul>

    <p class="purity">100%<br>Pure Natural<br>Collagen Protein</p>
    <p class="tagline">Excellent Source of Protein!</p>
    <p class="net-weight">Net Wt. 1 Lb (454 g)</p>
  </main>
</body>
</html>
```